Granite Ridge College-Pinecrest Welcome Week

I am the Student Activities Coordinator at Granite Ridge College-Pinecrest. For Welcome Week 2013, I need a standard poster 24x36 with the list of events happening. Our theme is based on the popular Friday Late Laughs video "We Got a Kite"
http://www.vidtrove.example/clip/Q4mZp8sLwTe
Our theme is:
We're at the 'Crest!
Welcome Week 2013
Graphics on the poster should reflect popular images/designs of FLL We Got a Kite. However, the boat should be a steamboat instead of the yacht image.
Unfortunately, I have a lot of text to fit on the poster. Traditionally we go with 3 margins listing events. I'm attaching the word document of events and our logo to this proposal. I'll also attach a few google images of "We Got a Kite" that align with the type of theme I'm looking for.
One last thing, our logo contains mountains listing all of the different campuses. Remove the campus names and mountains all together. Use simply the Colorado flag C and "Granite Ridge College".
Thanks for considering this brief!
Glen
Target Market(s)
Our college students love to ski and snowboard. In fact, one of our degrees is "Alpine Slope Commerce". Their ages are 18-22.
Industry/Entity Type
Events
Look and feel

```html
<!DOCTYPE html>
<html lang="en">
<head>
<meta charset="utf-8">
<title>Granite Ridge College-Pinecrest Welcome Week 2013</title>
<link rel="stylesheet" href="https://fonts.googleapis.com/css2?family=Arimo:wght@700&family=Roboto+Condensed:wght@400;700&display=swap">
<style>
  :root {
    --stage: #e6e3de;
    --navy: #1f3470;
    --navy-deep: #172a5e;
    --panel: rgba(28, 46, 108, 0.88);
    --panel-edge: rgba(120, 150, 210, 0.35);
    --yellow: #f2e43a;
    --white: #ffffff;
    --flag-red: #c8202f;
    --sea-dark: #1d3550;
    --sea-mid: #3f6283;
    --sky-top: #7ea2c6;
    --lake: #46709c;
    --shore: #6b6a66;
  }
  * { box-sizing: border-box; margin: 0; padding: 0; }
  html, body { width: 834px; height: 1200px; overflow: hidden; }
  body { background: var(--stage); position: relative; font-family: "Roboto Condensed", "Arial Narrow", sans-serif; }

  .poster { position: absolute; left: 16px; top: 0; width: 802px; height: 1200px; background: var(--navy); overflow: hidden; }

  .masthead { position: absolute; left: 0; top: 0; width: 100%; height: 127px; background: var(--navy); border-bottom: 3px solid var(--white); display: flex; align-items: center; justify-content: center; gap: 12px; }
  .masthead__dot { width: 66px; height: 66px; border-radius: 50%; background: var(--flag-red); }
  .masthead__name { font-family: "Roboto Condensed", sans-serif; font-weight: 700; color: var(--white); font-size: 27px; line-height: 27px; text-transform: uppercase; letter-spacing: 0.2px; }

  .hero-photo { position: absolute; left: 0; top: 130px; width: 100%; height: 300px;
    background: linear-gradient(180deg, var(--sea-mid) 0%, #5a7ea0 35%, var(--sea-dark) 100%); }
  .backdrop-photo { position: absolute; left: 0; top: 430px; width: 100%; height: 770px;
    background: linear-gradient(180deg, #3a5f90 0%, var(--sky-top) 38%, var(--lake) 62%, #5b6f84 82%, var(--shore) 100%); }

  .title { position: absolute; left: 0; top: 392px; width: 100%; text-align: center; color: var(--white); font-family: "Arimo", Arial, sans-serif; font-weight: 700; font-size: 32px; letter-spacing: -0.3px; text-shadow: 0 2px 4px rgba(0,0,0,0.45); }
  .title__year { font-size: 50px; vertical-align: -4px; }

  .day-panel { position: absolute; width: 220px; background: var(--panel); border: 1px solid var(--panel-edge); padding: 10px 14px; color: var(--white); }
  .col-1 { left: 32px; } .col-2 { left: 294px; } .col-3 { left: 557px; }
  .row-1 { top: 453px; height: 340px; }
  .row-2 { top: 808px; height: 382px; }
  .row-2.col-3 { height: 308px; }

  .day-panel__date { color: var(--yellow); font-weight: 700; font-size: 16px; line-height: 19px; margin-bottom: 7px; }
  .day-panel__date--later { margin-top: 12px; }
  .event { margin-bottom: 12px; font-size: 11px; line-height: 13px; }
  .event__name { color: var(--yellow); font-weight: 700; font-size: 11.5px; }
  .event__detail { color: var(--white); }
  .event--compact { margin-bottom: 6px; }

  .footnote { position: absolute; left: 14px; bottom: 36px; color: #e8ecf6; font-size: 10.5px; line-height: 13px; text-transform: uppercase; }
</style>
</head>
<body>
<main class="poster">
  <header class="masthead">
    <span class="masthead__dot"></span>
    <span class="masthead__name">Granite Ridge<br>College</span>
  </header>

  <div class="hero-photo" role="img" aria-label="Photograph of a white steamboat cruising across dark blue water"></div>
  <div class="backdrop-photo" role="img" aria-label="Faded photograph of students standing on a lakeshore beneath mountains"></div>

  <h1 class="title">We're at the 'Crest! Welcome Week <span class="title__year">2013</span></h1>

  <section class="day-panel col-1 row-1">
    <h2 class="day-panel__date">Thursday August 22</h2>
    <div class="event"><div class="event__name">Residence Hall Move-In</div><div class="event__detail">12:00pm-3:00pm<br>Ridge Hall</div></div>
    <div class="event"><div class="event__name">Brunch</div><div class="event__detail">10:00am-1:00pm<br>Dining Hall</div></div>
    <div class="event"><div class="event__name">International Students Orientation</div><div class="event__detail">3:00pm<br>Hawthorne 121</div></div>
    <div class="event"><div class="event__name">Dinner</div><div class="event__detail">5:00pm-6:30pm<br>Dining Hall<br>Hot Springs Waterslide Party<br>7:00pm-9:00pm<br>Pine Town Hot Springs</div></div>
  </section>

  <section class="day-panel col-2 row-1">
    <h2 class="day-panel__date">Saturday August 24</h2>
    <div class="event"><div class="event__name">Main Street Farmers Market</div><div class="event__detail">9:00am-2:00pm<br>6th &amp; Birch (walking dist.)</div></div>
    <div class="event"><div class="event__name">Brunch</div><div class="event__detail">10:00am-1:00pm<br>Dining Hall</div></div>
    <div class="event"><div class="event__name">Bluebell Park Hot Springs</div><div class="event__detail">2:00pm-5:00pm<br>Shuttle leaves Ridge Hall at 1:30pm</div></div>
    <div class="event"><div class="event__name">Dinner</div><div class="event__detail">5:00-6:00pm<br>Dining Hall</div></div>
    <div class="event"><div class="event__name">Free Movie on the Mountain:<br>Ember Trials</div><div class="event__detail">8:00pm<br>(PCT Buses to Resort,<br>5:35pm Last Bus)</div></div>
  </section>

  <section class="day-panel col-3 row-1">
    <h2 class="day-panel__date">Monday August 26</h2>
    <div class="event"><div class="event__name">Regular Dining Hall Hours Begin</div></div>
    <div class="event event--compact"><div class="event__detail">&ldquo;Being Alone Sucks!&rdquo;<br>9:00pm<br>Auditorium</div></div>
    <h2 class="day-panel__date day-panel__date--later">Tuesday August 27</h2>
    <div class="event"><div class="event__name">Newly Roommate Game</div><div class="event__detail">7:00pm-8:00pm<br>Ridge Hall: MPR</div></div>
    <div class="event event--compact"><div class="event__name">Free Gelato</div><div class="event__detail">8:00pm-9:00pm<br>Bello Gelato 7th and Alder</div></div>
    <h2 class="day-panel__date day-panel__date--later">Wednesday August 28</h2>
    <div class="event"><div class="event__name">Free Bowling</div><div class="event__detail">9:00pm<br>Summit Lanes</div></div>
  </section>

  <section class="day-panel col-1 row-2">
    <h2 class="day-panel__date">Friday August 23</h2>
    <div class="event"><div class="event__name">Breakfast</div><div class="event__detail">7:30am-9:00am<br>Dining Hall</div></div>
    <div class="event"><div class="event__name">Hike Trout Creek Falls</div><div class="event__detail">9:00am-11:30am<br>Shuttle leaves Ridge Hall at 8:30am</div></div>
    <div class="event"><div class="event__name">BBQ and Faculty Ice Cream Social</div><div class="event__detail">12:00pm-1:30pm<br>Dining Hall</div></div>
    <div class="event"><div class="event__name">Kick Off Party: Inflatables</div><div class="event__detail">1:30pm-4:00pm<br>Upper Parking Lot</div></div>
    <div class="event"><div class="event__name">Dinner</div><div class="event__detail">5:00pm-6:00pm<br>Dining Hall</div></div>
    <div class="event"><div class="event__name">Free Concert</div><div class="event__detail">7:00pm<br>Pinecrest Resort Base<br>(PCT Buses to Resort,<br>5:35pm Last Bus)</div></div>
  </section>

  <section class="day-panel col-2 row-2">
    <h2 class="day-panel__date">Sunday August 25</h2>
    <div class="event"><div class="event__name">Brunch</div><div class="event__detail">10:00am-1:00pm<br>Dining Hall</div></div>
    <div class="event"><div class="event__name">Alpine Slide/Volleyball</div><div class="event__detail">2:00pm-4:00pm<br>Meet at Larkin Hill</div></div>
    <div class="event"><div class="event__name">Dinner</div><div class="event__detail">5:00pm-6:00pm<br>Dining Hall</div></div>
    <div class="event"><div class="event__name">Mandatory All Hall Meeting</div><div class="event__detail">6:00pm<br>Auditorium</div></div>
    <div class="event"><div class="event__name">RHA Super Sunday Program</div><div class="event__detail">8:00pm<br>Ridge Hall: MPR</div></div>
  </section>

  <section class="day-panel col-3 row-2">
    <h2 class="day-panel__date">Thursday August 29</h2>
    <div class="event"><div class="event__name">Club Fair</div><div class="event__detail">10:00am-2:00pm<br>Dining Hall</div></div>
    <div class="event event--compact"><div class="event__name">Black Light Dodgeball</div><div class="event__detail">9:00pm<br>Gym</div></div>
    <h2 class="day-panel__date day-panel__date--later">Friday August 30</h2>
    <div class="event"><div class="event__name">Late Night Climbing</div><div class="event__detail">9:00pm<br>Gym</div></div>
    <p class="footnote">All events *<br>are free unless<br>otherwise noted</p>
  </section>
</main>
</body>
</html>
```